Webdesign für Helga Stirnweis, Corvell Management
Zielgruppe
Unternehmensberatung, Schwerpunkt Leadership development, Personalentwicklung und -beratung, Karrierecoaching, es soll auf jeder Seite auch ein link sein zur Englischseite;
ungefährer startseitetext: Mein Ziel: Begeistern und Befähigen;
Lernen und Veränderungen entstehen aus Reflexion. Der Betreffende tritt einen Schritt zurück, schaut auf das bisherige Verhalten und stellt sich die Frage, ob er dieses Verhalten und die Auswirkungen dieses Verhaltens in Zukunft wieder wählen möchten.
Leadership
• Fähigkeiten bei ihren MitarbeiterInnen aktivieren, welche sie sich selbst vielleicht nicht zugetraut hätten.
• Die Vielfalt unter ihren MitarabeiterInnen schätzen und die Unterschiede als Ressourcen nutzen.
• Eine Organisation schaffen, der ihre MitarbeiterInnen gerne angehören und in die sie gerne aktiv ihre Kompetenzen und ihr Potenzial einbringen.
Coaching:
Mein Ziel ist, Sie in ihren Herausforderung und Veränderungen zu unterstützen. Bei Veränderungen in ihrem beruflichen Werdegang oder den täglichen Herausforderungen, z.B. mit dem Zeitmanagement, werde ich Sie begleiten und beharrlich fordern.
Aufgabenstellung
es sollen Fotos (trainingsituationen) integriert werden, Schrift Geneva und Avenir Next gefallen mir, Logo vorhanden - in Farbe nachtblau/nightblue und schwarz;
gute Freunde beschreiben mich als: gewissenhaft, integrierend, beharrlich, ausdrucksstark, vertrauensvoll, offen, durchgreifend;

```html
<!DOCTYPE html>
<html lang="de">
<head>
<meta charset="utf-8">
<title>Corvell Management – Helga Stirnweis</title>
<link href="https://fonts.googleapis.com/css2?family=Montserrat:wght@400;500;600;700&family=Raleway:wght@400;500&family=Crimson+Text:ital@1&family=Lato:ital,wght@1,400&display=swap" rel="stylesheet">
<style>
:root{
  --night:#413a87;
  --night-deep:#3b347f;
  --ink:#1e1e1e;
  --text:#555;
  --muted:#777;
  --band:#f4f4f4;
  --line:#dcdcdc;
  --white:#fff;
}
*{margin:0;padding:0;box-sizing:border-box}
html,body{width:1200px;height:3021px;overflow:hidden;background:var(--white)}
body{position:relative;font-family:"Raleway",sans-serif;color:var(--text)}
.abs{position:absolute}
.caps{font-family:"Montserrat",sans-serif;text-transform:uppercase}

/* header */
.site-header{left:0;top:0;width:1200px;height:82px;background:var(--white)}
.brand{left:106px;top:22px;display:flex;align-items:center;gap:8px}
.brand-dot{width:26px;height:26px;border-radius:50%;background:var(--night)}
.brand-name{font-family:"Montserrat",sans-serif;font-weight:600;font-size:24px;color:var(--night)}
.main-nav a{position:absolute;top:40px;font-family:"Montserrat",sans-serif;font-size:12px;letter-spacing:1.5px;color:#333;text-decoration:none;font-weight:500}
.search-icon{left:1081px;top:40px}

/* hero */
.hero{left:0;top:82px;width:1200px;height:425px;background:linear-gradient(100deg,#5b5e6b 0%,#c9c3bb 30%,#ece8e2 50%,#a39587 75%,#6b5146 100%)}
.hero-box{left:323px;top:191px;width:547px;height:145px;background:rgba(110,110,110,.72);text-align:center;color:var(--white)}
.hero-title{font-family:"Montserrat",sans-serif;font-weight:700;font-size:40px;letter-spacing:6px;margin-top:30px;line-height:1}
.hero-sub{font-family:"Montserrat",sans-serif;font-weight:700;font-size:24px;letter-spacing:4px;margin-top:18px;line-height:1}

/* intro */
.intro-photo{left:106px;top:575px;width:422px;height:270px;background:linear-gradient(160deg,#d8d6d2 0%,#8c7a6b 45%,#b0794a 75%,#5a3a2a 100%)}
.intro-kicker{left:611px;top:574px;font-family:"Crimson Text",serif;font-style:italic;font-size:12px;color:#444}
.intro-title{left:611px;top:605px;font-family:"Montserrat",sans-serif;font-weight:600;font-size:20px;letter-spacing:3px;color:var(--ink)}
.intro-text{left:611px;top:645px;width:480px;font-size:12.5px;line-height:25.5px;color:#555}
.btn{display:block;background:var(--night);color:var(--white);text-align:center;font-family:"Montserrat",sans-serif;font-weight:600;text-transform:uppercase;font-size:12px;letter-spacing:1px;text-decoration:none}
.intro-btn{left:611px;top:772px;width:255px;height:41px;line-height:41px}

/* services */
.services{left:0;top:910px;width:1200px;height:447px;background:var(--band)}
.section-title{width:1200px;left:0;text-align:center;font-family:"Montserrat",sans-serif;font-weight:600;font-size:32px;color:var(--ink);letter-spacing:-.5px}
.service{width:240px;text-align:center}
.service-icon{width:86px;height:86px;border-radius:50%;background:var(--white);border:1px solid #ddd;margin:0 auto;display:flex;align-items:center;justify-content:center}
.service-name{margin-top:31px;font-family:"Montserrat",sans-serif;font-weight:600;font-size:10px;letter-spacing:.8px;color:#222;text-transform:uppercase}
.service-text{margin-top:12px;font-size:12.5px;line-height:21px;color:#555}
.service .btn{width:118px;height:34px;line-height:34px;font-size:11px;margin:22px auto 0}

/* testimonials */
.quote-card{width:429px;height:232px;border:1px solid var(--line);background:var(--white)}
.avatar{width:96px;height:96px;border-radius:50%;background:linear-gradient(135deg,#e9d9cc,#8b6e5c)}
.quote-text{left:77px;top:30px;width:330px;font-family:"Crimson Text",serif;font-style:italic;font-size:12.5px;line-height:25.5px;color:#555}
.quote-name{left:77px;top:160px;font-family:"Montserrat",sans-serif;font-size:10px;font-weight:500;color:#222;text-transform:uppercase}
.quote-role{left:77px;top:177px;font-family:"Crimson Text",serif;font-style:italic;font-size:11px;color:#777}
.rule{left:0;top:1803px;width:1200px;height:1px;background:var(--line)}

/* blog */
.post{width:313px}
.post-photo{position:relative;height:218px}
.post-date{position:absolute;left:0;bottom:32px;width:49px;height:44px;background:var(--night);color:var(--white);text-align:center;font-family:"Montserrat",sans-serif;font-weight:500;font-size:13px;line-height:16px;padding-top:6px}
.post-title{margin-top:24px;font-family:"Montserrat",sans-serif;font-weight:500;font-size:17px;color:var(--ink)}
.post-text{margin-top:13px;font-size:11.5px;line-height:20px;color:#555;height:60px}
.post-more{margin-top:12px;text-align:right;font-family:"Montserrat",sans-serif;font-size:10.5px;color:#222}

/* contact */
.contact-photo{left:0;top:2362px;width:600px;height:507px;background:radial-gradient(ellipse at 35% 35%,#f2f0ea 0%,#b7b2a6 35%,#4f5d70 65%,#2d3340 100%)}
.social{top:2800px;width:34px;height:34px;border-radius:50%;background:rgba(255,255,255,.25)}
.social.active{background:var(--night)}
.contact-panel{left:600px;top:2362px;width:600px;height:507px;background:#f5f4f2}
.contact-title{left:643px;top:2408px;font-family:"Montserrat",sans-serif;font-weight:600;font-size:30px;color:var(--ink)}
.contact-intro{left:643px;top:2463px;width:450px;font-family:"Lato",sans-serif;font-style:italic;font-size:14px;line-height:21px;color:#666}
.field{left:643px;width:451px;background:var(--white);font-family:"Lato",sans-serif;font-style:italic;font-size:10px;letter-spacing:.8px;color:#333;text-transform:uppercase;padding:12px 12px}
.field span{color:var(--night)}
.send-btn{left:959px;top:2809px;width:135px;height:32px;border:2px solid #c9c9c9;background:var(--white);text-align:center;line-height:28px;font-family:"Montserrat",sans-serif;font-size:11px;letter-spacing:2px;color:#333}

/* footer */
.site-footer{left:0;top:2869px;width:1200px;height:152px;background:var(--night-deep);border-top:2px solid #6a64a6}
.footer-nav a{position:absolute;top:57px;font-family:"Montserrat",sans-serif;font-weight:600;font-size:12px;letter-spacing:1.5px;color:var(--white);text-decoration:none}
.copyright{top:95px;width:1200px;text-align:center;font-family:"Montserrat",sans-serif;font-weight:500;font-size:9.5px;letter-spacing:1px;color:var(--white)}
</style>
</head>
<body>

<header class="site-header abs">
  <div class="brand abs"><span class="brand-dot"></span><span class="brand-name">Corvell</span></div>
  <nav class="main-nav">
    <a style="left:500px">HOME</a>
    <a style="left:609px">ABOUT US</a>
    <a style="left:742px">SERVICES <svg width="7" height="5" viewBox="0 0 7 5"><path d="M1 1l2.5 2.5L6 1" stroke="#333" fill="none"/></svg></a>
    <a style="left:880px">GOAL</a>
    <a style="left:979px">CONTACT</a>
  </nav>
  <svg class="search-icon abs" width="12" height="12" viewBox="0 0 12 12"><circle cx="5" cy="5" r="3.6" stroke="#222" stroke-width="1.8" fill="none"/><path d="M7.6 7.6L11 11" stroke="#222" stroke-width="2"/></svg>
</header>

<section class="hero abs" role="img" aria-label="Foto: Trainerin präsentiert vor aufmerksamen Seminarteilnehmenden"></section>
<div class="hero-box abs">
  <div class="hero-title">MEIN ZIEL:</div>
  <div class="hero-sub">BEGEISTERN UND BEFÄHIGEN</div>
</div>

<div class="intro-photo abs" role="img" aria-label="Foto: Publikum in einem Seminarraum von hinten"></div>
<p class="intro-kicker abs">Welcome to Helga Stirnweis, Corvell Management</p>
<h2 class="intro-title abs">GROWTH UP YOUR BUSINESS</h2>
<p class="intro-text abs">There are many variations of passages of Lorem Ipsum available, but the majority have suffered alteration in some form, by injected humour, or randomised words which don't look even slightly believable. If you are going to use a passage of Lorem Ipsum, you need to be sure .</p>
<a class="btn intro-btn abs">LEARN MORE</a>

<section class="services abs"></section>
<h2 class="section-title abs" style="top:975px">Our Services</h2>
<div class="service abs" style="left:99px;top:1050px">
  <div class="service-icon"><svg width="40" height="34" viewBox="0 0 40 34"><rect x="13" y="2" width="14" height="7" rx="2" fill="none" stroke="#111" stroke-width="3"/><rect x="1" y="8" width="38" height="25" rx="3" fill="#111"/><path d="M3 17h34" stroke="#fff" stroke-width="2"/></svg></div>
  <div class="service-name">Business Consultancy</div>
  <div class="service-text">Lorem ipsum dolor sit amet,<br>consectetuer adipiscing elit,</div>
  <a class="btn">Learn More</a>
</div>
<div class="service abs" style="left:351px;top:1050px">
  <div class="service-icon"><svg width="42" height="40" viewBox="0 0 42 40"><rect x="2" y="3" width="38" height="28" fill="none" stroke="#111" stroke-width="2.5"/><path d="M2 9h38" stroke="#111" stroke-width="2.5"/><circle cx="20" cy="28" r="7" fill="#111"/><circle cx="20" cy="28" r="2.5" fill="#fff"/></svg></div>
  <div class="service-name">Leadership Development</div>
  <div class="service-text">Lorem ipsum dolor sit amet,<br>consectetuer adipiscing elit,</div>
  <a class="btn">Learn More</a>
</div>
<div class="service abs" style="left:607px;top:1050px">
  <div class="service-icon"><svg width="34" height="36" viewBox="0 0 34 36"><circle cx="17" cy="11" r="8" fill="#111"/><path d="M3 34c0-9 6-14 14-14s14 5 14 14z" fill="#111"/></svg></div>
  <div class="service-name">Staff Development &amp; Consulting</div>
  <div class="service-text">Lorem ipsum dolor sit amet,<br>consectetuer adipiscing elit,</div>
  <a class="btn">Learn More</a>
</div>
<div class="service abs" style="left:860px;top:1050px">
  <div class="service-icon"><svg width="46" height="42" viewBox="0 0 46 42"><circle cx="8" cy="9" r="4.5" fill="#111"/><path d="M3 16h10l10-6 1.5 2-9 7v22H11V30H8v11H4z" fill="#111"/><rect x="22" y="3" width="22" height="17" fill="none" stroke="#111" stroke-width="2.5"/><circle cx="35" cy="11" r="3.5" fill="#111"/></svg></div>
  <div class="service-name">Career Coaching</div>
  <div class="service-text">Lorem ipsum dolor sit amet,<br>consectetuer adipiscing elit,</div>
  <a class="btn">Learn More</a>
</div>

<h2 class="section-title abs" style="top:1417px">What they said?</h2>
<div class="quote-card abs" style="left:158px;top:1505px">
  <p class="quote-text abs">" "Sed ut perspiciatis unde omnis iste natus error sit voluptatem accusantium doloremque laudantium, totam rem aperiam, eaque ipsa quae ab illo inventore veritatis et quasi architecto beatae vitae dicta sunt explicabo. "</p>
  <div class="quote-name abs">Tobias Renner</div>
  <div class="quote-role abs">CEO/ Founder Orchard Labs</div>
</div>
<div class="avatar abs" style="left:105px;top:1554px" role="img" aria-label="Porträtfoto einer Kundin"></div>
<div class="quote-card abs" style="left:665px;top:1505px">
  <p class="quote-text abs">" "Sed ut perspiciatis unde omnis iste natus error sit voluptatem accusantium doloremque laudantium, totam rem aperiam, eaque ipsa quae ab illo inventore veritatis et quasi architecto beatae vitae dicta sunt explicabo. "</p>
  <div class="quote-name abs">Miriam Holt</div>
  <div class="quote-role abs">CEO/ Founder Nordwind Tech</div>
</div>
<div class="avatar abs" style="left:613px;top:1554px" role="img" aria-label="Porträtfoto eines Kunden"></div>

<div class="rule abs"></div>

<h2 class="section-title abs" style="top:1863px">Latest Blog</h2>
<article class="post abs" style="left:106px;top:1939px">
  <div class="post-photo" role="img" aria-label="Foto: Präsentation vor einer Leinwand im Besprechungsraum" style="background:linear-gradient(180deg,#eeeeee 0%,#d9d8d6 55%,#8c8f99 100%)"><div class="post-date">08<br>JUN</div></div>
  <h3 class="post-title">Brooklyn</h3>
  <p class="post-text">Sed ut perspiciatis unde omnis iste natus error sit voluptatem accusantium doloremque laudantium, totam rem aperiam.</p>
  <div class="post-more">Read More &nbsp;›</div>
</article>
<article class="post abs" style="left:443px;top:1939px">
  <div class="post-photo" role="img" aria-label="Foto: applaudierendes Seminarpublikum" style="background:linear-gradient(135deg,#b9b3ad 0%,#e6cdb0 40%,#d9c24a 75%,#7a6a5a 100%)"><div class="post-date">07<br>JUN</div></div>
  <h3 class="post-title">Larkfield Juicery</h3>
  <p class="post-text">On the other hand, we denounce with righteous indignation and dislike men who are so beguiled and demoralized</p>
  <div class="post-more">Read More &nbsp;›</div>
</article>
<article class="post abs" style="left:781px;top:1939px">
  <div class="post-photo" role="img" aria-label="Foto: Mikrofon vor einem Konferenzsaal" style="background:linear-gradient(180deg,#f1f1f1 0%,#c9ccd2 45%,#6f7a8c 100%)"><div class="post-date">06<br>JUN</div></div>
  <h3 class="post-title">Hello Itaewon Project</h3>
  <p class="post-text">Lorem ipsum dolor sit amet, consectetur adipiscing elit, sed do eiusmod tempor incididunt ut labore et dolore magna aliqua. Ut enim ad minim veniam,</p>
  <div class="post-more">Read More &nbsp;›</div>
</article>

<div class="contact-photo abs" role="img" aria-label="Unscharfes Foto eines Seminarsaals mit Publikum"></div>
<span class="social abs" style="left:68px"></span>
<span class="social active abs" style="left:111px"></span>
<span class="social abs" style="left:155px"></span>
<span class="social abs" style="left:199px"></span>
<span class="social abs" style="left:243px"></span>
<span class="social abs" style="left:287px"></span>

<section class="contact-panel abs"></section>
<h2 class="contact-title abs">Contact us</h2>
<p class="contact-intro abs">Please don't hesitate to contact me if you have any questions, commnets or messages. I'll try to respond to everything!</p>
<div class="field abs" style="top:2534px;height:33px"><span>*</span> Name</div>
<div class="field abs" style="top:2585px;height:33px"><span>*</span> Email</div>
<div class="field abs" style="top:2635px;height:33px">Subject</div>
<div class="field abs" style="top:2686px;height:104px">Conent</div>
<div class="send-btn abs">SEND ME</div>

<footer class="site-footer abs">
  <nav class="footer-nav">
    <a style="left:325px">HOME</a>
    <a style="left:434px">ABOUT US</a>
    <a style="left:567px">SERVICES</a>
    <a style="left:704px">GOAL</a>
    <a style="left:803px">CONTACT</a>
  </nav>
  <p class="copyright abs">© 2016 CORVELL MANAGEMENT. POWERED BY PIXELHAUS</p>
</footer>

</body>
</html>
```